serious, thorough, light and simple - that's my advice and mediations

My business card should combine my logo (uploaded file) and my homepage (https://fellor-mediation.webnestsite.com).

Contact Information for Business Card

Name: Sabine Fellor di Vanti
Phone: 076 412 58 94
mail: sfellor@postkiv.ch
web: www.fellor-di-vanti.ch

```html
<!DOCTYPE html>
<html lang="de">
<head>
<meta charset="utf-8">
<title>Visitenkarte – Sabine Fellor di Vanti</title>
<link href="https://fonts.googleapis.com/css2?family=Arimo:wght@400;700&display=swap" rel="stylesheet">
<style>
  :root {
    --backdrop: #ebebeb;
    --card-white: #f3f3f3;
    --brand-blue: #253a8a;
    --brand-green: #0c6b3a;
    --brand-gold: #a8864a;
    --text-grey: #9a9a9a;
    --divider: #a8a8a8;
    --gradient-start: #26388a;
    --gradient-mid: #1b4f6e;
    --gradient-end: #066a35;
    --white: #ffffff;
  }
  * { margin: 0; padding: 0; box-sizing: border-box; }
  html, body {
    width: 1200px; height: 1200px; overflow: hidden;
    background: var(--backdrop);
    font-family: "Arimo", Arial, sans-serif;
  }
  .card {
    position: absolute;
    left: 227px;
    width: 746px;
    height: 425px;
  }
  .card--front { top: 135px; background: var(--card-white); }
  .card--back {
    top: 639px;
    background: linear-gradient(90deg, var(--gradient-start) 2%, var(--gradient-mid) 50%, var(--gradient-end) 98%);
  }

  .brand {
    position: absolute;
    display: flex; flex-direction: column; align-items: center;
  }
  .brand__row { display: flex; align-items: center; gap: 10px; }
  .brand__dot { border-radius: 50%; flex: none; }
  .brand__name { font-weight: 400; line-height: 1.15; white-space: nowrap; }
  .brand__tagline {
    font-weight: 400; text-transform: uppercase; white-space: nowrap;
  }

  .card--front .brand { left: 106px; top: 200px; width: 240px; }
  .card--front .brand__dot { width: 20px; height: 20px; background: var(--brand-blue); }
  .card--front .brand__name { font-size: 31px; color: var(--brand-gold); }
  .card--front .brand__tagline {
    margin-top: 26px; font-size: 8px; letter-spacing: 2.4px; color: var(--brand-green);
  }

  .divider {
    position: absolute; left: 373px; top: 151px;
    width: 1px; height: 124px; background: var(--divider);
  }

  .contact { position: absolute; left: 401px; top: 150px; }
  .contact__name {
    font-size: 21px; font-weight: 700; letter-spacing: -0.2px;
    color: var(--brand-blue); white-space: nowrap;
  }
  .contact__name .accent { color: var(--brand-green); }
  .contact__list { list-style: none; margin-top: 37px; }
  .contact__item {
    display: flex; align-items: center; gap: 7px;
    font-size: 16px; line-height: 21.5px; color: var(--text-grey);
  }
  .contact__icon { width: 14px; height: 14px; flex: none; }

  .card--back .brand { left: 206px; top: 210px; width: 337px; }
  .card--back .brand__dot { width: 28px; height: 28px; background: var(--white); }
  .card--back .brand__name { font-size: 44px; color: var(--white); }
  .card--back .brand__tagline {
    margin-top: 34px; font-size: 11px; letter-spacing: 3.6px; color: var(--white);
  }
</style>
</head>
<body>
  <section class="card card--front" aria-label="Vorderseite">
    <div class="brand">
      <div class="brand__row">
        <span class="brand__dot"></span>
        <span class="brand__name">Wege im Dialog</span>
      </div>
      <span class="brand__tagline">Zuhören, Verstehen, Lösen</span>
    </div>

    <div class="divider"></div>

    <div class="contact">
      <p class="contact__name">Sabine Fellor <span class="accent">di Vanti</span></p>
      <ul class="contact__list">
        <li class="contact__item">
          <svg class="contact__icon" viewBox="0 0 24 24" aria-hidden="true">
            <path fill="#0c6b3a" d="M6.6 10.8a15.1 15.1 0 0 0 6.6 6.6l2.2-2.2a1 1 0 0 1 1-.25 11.4 11.4 0 0 0 3.6.57 1 1 0 0 1 1 1V20a1 1 0 0 1-1 1A17 17 0 0 1 3 4a1 1 0 0 1 1-1h3.5a1 1 0 0 1 1 1c0 1.25.2 2.45.57 3.57a1 1 0 0 1-.25 1z"/>
            <path fill="none" stroke="#0c6b3a" stroke-width="1.8" d="M14 3a7 7 0 0 1 7 7M14 6.5a3.5 3.5 0 0 1 3.5 3.5"/>
          </svg>
          076 412 58 94
        </li>
        <li class="contact__item">
          <svg class="contact__icon" viewBox="0 0 24 24" aria-hidden="true">
            <rect x="2" y="5" width="20" height="14" fill="none" stroke="#0c6b3a" stroke-width="2"/>
            <path d="M2 5l10 8 10-8M2 19l7.5-7M22 19l-7.5-7" fill="none" stroke="#0c6b3a" stroke-width="1.8"/>
          </svg>
          sfellor@postkiv.ch
        </li>
        <li class="contact__item">
          <svg class="contact__icon" viewBox="0 0 24 24" aria-hidden="true">
            <g fill="none" stroke="#0c6b3a" stroke-width="1.8">
              <circle cx="12" cy="12" r="10"/>
              <ellipse cx="12" cy="12" rx="4.5" ry="10"/>
              <path d="M2 12h20M4 6.5h16M4 17.5h16"/>
            </g>
          </svg>
          www.fellor-di-vanti.ch
        </li>
      </ul>
    </div>
  </section>

  <section class="card card--back" aria-label="Rückseite">
    <div class="brand">
      <div class="brand__row">
        <span class="brand__dot"></span>
        <span class="brand__name">Wege im Dialog</span>
      </div>
      <span class="brand__tagline">Zuhören, Verstehen, Lösen</span>
    </div>
  </section>
</body>
</html>
```